Redesign of page from emergency manual

Please redesign this PDF to look better. Please don't include any stock photos. It must be legible. Making some words bold is probably a good idea.

Here are some things I like :

https://tarrowbooks.com.au/collections/frontpage/products/the-plk-v2-ebook

https://img-cd.vostramediafiles.com/qa-ejkwPLOTYY_SuCKbZNu411Qwgjv8YssPxEdzXN93hDkSRjLXK8WmfgbmrJW4ZZ3yUPK=w1052-h592-rw

```html
<!DOCTYPE html>
<html lang="en">
<head>
<meta charset="utf-8">
<title>Hypertension, Acute</title>
<link href="https://fonts.googleapis.com/css2?family=Bebas+Neue&family=Oswald:wght@500&family=Roboto:ital,wght@0,400;0,700;0,900;1,400;1,700&family=Roboto+Condensed:ital,wght@0,400;0,500;0,700;1,400;1,700&display=swap" rel="stylesheet">
<style>
:root{
  --paper:#f3f2ef;
  --ink:#1f1f1f;
  --red:#d8262f;
  --yellow:#f3ea00;
  --pink:#f4d3d8;
  --pink-soft:#f8e4e7;
  --grey:#dadada;
  --grey-dark:#c9c9c9;
  --line:#2a2a2a;
}
*{box-sizing:border-box;margin:0;padding:0}
html,body{width:925px;height:1200px;overflow:hidden}
body{background:var(--paper);color:var(--ink);font-family:"Roboto",Arial,sans-serif;position:relative}
.abs{position:absolute}

/* header */
.header-art{left:52px;top:68px;width:190px;height:150px;border-radius:10px;background:linear-gradient(135deg,#f0c4c7 0%,#e6d6d6 55%,#d4d2d0 100%)}
.title{left:254px;top:68px;font-family:"Bebas Neue",sans-serif;font-size:90px;line-height:1;letter-spacing:.3px;color:var(--ink)}
.subtitle{left:246px;top:154px;width:622px;height:22px;border-radius:11px;background:var(--ink);color:#fff;font-size:15px;line-height:22px;text-align:center}
.contact{left:258px;top:185px;width:600px;text-align:center;font-family:"Oswald",sans-serif;font-weight:500;font-size:14.5px;letter-spacing:1.3px}

/* intro box */
.intro{left:48px;top:261px;width:436px;height:241px;border:2px solid var(--line);border-radius:12px;overflow:hidden}
.intro-lead{height:110px;padding:4px 20px 0;font-family:"Roboto Condensed",sans-serif;font-weight:500;font-size:21px;line-height:25px;border-bottom:2px solid var(--line)}
.hl{background:var(--yellow);font-weight:700;font-style:italic;padding:0 3px}
.intro-cells{display:flex;height:129px}
.cuff{width:219px;border-right:2px solid var(--line);text-align:center;padding-top:6px;font-family:"Roboto Condensed",sans-serif;font-style:italic;font-weight:500;font-size:15px;line-height:17px}
.cuff-value{font-family:"Roboto",sans-serif;font-style:normal;font-weight:900;font-size:72px;line-height:72px;letter-spacing:-1px}
.aline{flex:1;text-align:center;padding-top:8px;font-family:"Roboto Condensed",sans-serif}
.aline-head{font-size:22px;font-weight:500;line-height:22px}
.aline-sub{font-size:13px;font-weight:700;line-height:15px}
.aline-note{font-size:15px;font-weight:500;line-height:17px;margin-top:4px}

/* bp table */
.bp{left:498px;top:261px;width:378px;height:241px;border:2px solid var(--line);border-radius:12px;overflow:hidden;background:#fff}
.bp-head{height:86px;background:var(--grey);border-bottom:2px solid var(--line);text-align:center;padding-top:14px;font-family:"Roboto Condensed",sans-serif;font-weight:500;font-size:22px;line-height:28px}
.bp table{width:100%;border-collapse:collapse;font-family:"Roboto Condensed",sans-serif}
.bp th{height:38px;font-size:22px;font-weight:500;border-bottom:2px solid var(--line);background:#fff}
.bp td{height:38.5px;font-size:15px;text-align:center;border-top:2px solid var(--line)}
.bp th+th,.bp td+td{border-left:2px solid var(--line)}
.bp tr:nth-child(2) td{border-top:none}
.bp td{background:#ececec}
.bp td+td{background:var(--grey-dark)}
.bp tr:nth-child(odd) td{background:#e4e4e4}
.bp tr:nth-child(odd) td+td{background:#d3d3d3}

/* caution */
.caution{left:100px;top:527px;width:778px;height:85px;background:var(--red);border-radius:12px;padding:8px 18px 0 57px;color:#fff;font-family:"Roboto Condensed",sans-serif;font-style:italic;font-size:16.5px;line-height:22px}
.caution b{color:var(--yellow);font-style:normal;font-weight:700}
.warn{left:16px;top:516px;width:132px;height:110px}

/* action */
.action{left:385px;top:625px;width:177px;height:33px;background:var(--red);color:#fff;font-family:"Roboto",sans-serif;font-weight:900;font-size:29px;line-height:34px;text-align:center;letter-spacing:.5px}
.action-panel{left:48px;top:671px;width:828px;height:291px;background:linear-gradient(var(--pink),var(--pink-soft));border-radius:70px 70px 0 0}
.connectors{left:0;top:655px;width:925px;height:60px}
.classes{left:48px;top:700px;width:828px;height:262px;display:flex}
.class{flex:1;padding:0 4px 0 10px;border-left:1px solid #d79aa2}
.class:first-child{border-left:none;flex:0 0 212px}
.class:nth-child(2){flex:0 0 212px}
.class:nth-child(3){flex:0 0 210px}
.class-name{text-align:center;font-family:"Roboto",sans-serif;font-weight:700;font-size:17.5px;line-height:20px;height:56px;padding-top:6px}
.drug{margin-bottom:12px}
.drug-name{font-weight:700;font-size:18.5px;line-height:19px;padding-left:12px;position:relative}
.drug-name::before{content:"";position:absolute;left:0;top:7px;width:5px;height:5px;border-radius:50%;background:var(--red)}
.drug-name small{font-size:12.5px;font-style:italic}
.dose{padding-left:12px;margin-top:5px;font-size:13.5px;line-height:16px}
.dose i{font-weight:700;font-family:"Roboto Condensed",sans-serif}

/* differential */
.ddx{left:48px;top:965px;width:828px;height:185px;border:2px solid var(--line);border-radius:12px;overflow:hidden;background:linear-gradient(var(--pink-soft),#fff)}
.ddx-head{height:48px;background:var(--grey);border-bottom:2px solid var(--line);padding:3px 18px;font-family:"Roboto Condensed",sans-serif;font-weight:500;font-size:32px;line-height:40px;position:relative}
.ddx-head svg{position:absolute;right:28px;top:12px}
.ddx-cols{display:flex;height:133px}
.ddx-col{padding:12px 14px 0;font-size:15.5px;line-height:18px}
.ddx-col+.ddx-col{border-left:2px solid var(--line)}
.ddx-col:nth-child(1){width:272px}
.ddx-col:nth-child(2){width:282px}
.ddx-col:nth-child(3){flex:1}
.ddx-col li{list-style:none;padding-left:14px;position:relative;padding-bottom:8px;margin-bottom:9px;border-bottom:1.5px solid var(--line)}
.ddx-col li:last-child{border-bottom:none}
.ddx-col li::before{content:"•";position:absolute;left:0}
.ddx-col em{color:#333}
</style>
</head>
<body>

<div class="abs header-art" role="img" aria-label="Heart symbol with ECG trace running beneath the title"></div>
<h1 class="abs title">HYPERTENSION, ACUTE</h1>
<div class="abs subtitle">Sustained high blood pressure refractory to treating reversible causes</div>
<div class="abs contact">WWW.PAEDSCRISISCARDS.ORG | HELLO@PAEDSCRISISCARDS.ORG | 015 482 6093</div>

<section class="abs intro">
  <p class="intro-lead">In pediatrics, <span class="hl">hypertension is almost always treated by addressing likely causes</span> such as light anesthesia or measurement error:</p>
  <div class="intro-cells">
    <div class="cuff">Ensure correct BP cuff<br>size : cuff bladder width<div class="cuff-value">40%</div>of limb circumference</div>
    <div class="aline">
      <div class="aline-head">Ensure arterial line</div>
      <div class="aline-sub">transducer is at level of heart</div>
      <svg width="60" height="26" viewBox="0 0 60 26" aria-hidden="true"><path d="M2 15 H24 L29 3 L34 23 L38 15 H58" fill="none" stroke="var(--ink)" stroke-width="2.5"/></svg>
      <div class="aline-note">Consider placing arterial<br>line if not already present</div>
    </div>
  </div>
</section>

<section class="abs bp">
  <div class="bp-head">HYPERTENSIVE<br>BLOOD PRESSURE RANGE*</div>
  <table>
    <tr><th>Age (yr)</th><th>Systolic</th><th>Diastolic</th></tr>
    <tr><td>Newborn</td><td>&gt;97</td><td>&gt;70</td></tr>
    <tr><td>1-3</td><td>&gt;105</td><td>&gt;61</td></tr>
    <tr><td>4-12</td><td>&gt;113</td><td>&gt;86</td></tr>
  </table>
</section>

<div class="abs caution"><b>CAUTION:</b> Anti-hypertensive drugs are almost never needed for routine pediatric cases. These medications are used almost exclusively for specialized cardiac, neurosurgical, or endocrine (pheochromocytoma) cases. Consult an expert before use. Rule-out increased ICP.</div>
<svg class="abs warn" viewBox="0 0 132 110" aria-hidden="true">
  <path d="M66 6 L126 104 H6 Z" fill="var(--yellow)" stroke="var(--ink)" stroke-width="6" stroke-linejoin="round"/>
  <rect x="61" y="42" width="10" height="34" fill="var(--ink)"/>
  <rect x="61" y="82" width="10" height="10" fill="var(--ink)"/>
</svg>

<div class="abs action-panel"></div>
<svg class="abs connectors" viewBox="0 0 925 60" aria-hidden="true">
  <g fill="none" stroke="var(--ink)" stroke-width="1.5" stroke-dasharray="4 3">
    <path d="M455 5 V14 L449 19 H167 L161 25 V46"/>
    <path d="M468 5 V22 L462 27 H365 L359 33 V46"/>
    <path d="M480 5 V22 L486 27 H572 L578 33 V46"/>
    <path d="M492 5 V14 L498 19 H767 L773 25 V46"/>
  </g>
  <g fill="var(--ink)"><circle cx="161" cy="48" r="5"/><circle cx="359" cy="48" r="5"/><circle cx="578" cy="48" r="5"/><circle cx="773" cy="48" r="5"/></g>
</svg>
<div class="abs action">ACTION</div>

<section class="abs classes">
  <div class="class">
    <h3 class="class-name">Direct Smooth<br>Muscle Relaxation</h3>
    <div class="drug"><div class="drug-name">Sodium<br>nitroprusside</div><div class="dose">0.5-10<br><i>MICROgrams/kg/min</i></div></div>
    <div class="drug"><div class="drug-name">HydrALAZINE</div><div class="dose">0.1-0.2 <i>mg/kg</i><br><i>(adult dose 5-10 mg)</i></div></div>
  </div>
  <div class="class">
    <h3 class="class-name">B-adrenergic<br>Blockade</h3>
    <div class="drug"><div class="drug-name">Esmolol</div><div class="dose">100-500 <i>MICROgrams/kg</i><br>over 5 min, then<br>25-300 <i>MICROgrams/kg/min</i></div></div>
    <div class="drug"><div class="drug-name">Labetalol <small>(also a effect)</small></div><div class="dose">0.2-1 <i>mg/kg q 10 min;</i><br>0.4-3 <i>mg/kg/hour (infusion)</i></div></div>
  </div>
  <div class="class">
    <h3 class="class-name">Calcium Channel<br>Blockade</h3>
    <div class="drug" style="margin-bottom:40px"><div class="drug-name">niCARdapine</div><div class="dose">0.5-5<br><i>MICROgrams/kg/min</i></div></div>
    <div class="drug"><div class="drug-name">Clevidipine</div><div class="dose">0.5-3.5<br><i>MICROgrams/kg/min</i></div></div>
  </div>
  <div class="class">
    <h3 class="class-name">D1-dopamine<br>Agonist</h3>
    <div class="drug"><div class="drug-name">Fenoldopam</div><div class="dose">0.2-0.8<br><i>MICROgrams/kg/min</i></div></div>
  </div>
</section>

<section class="abs ddx">
  <h2 class="ddx-head">Consider Differential (Partial)
    <svg width="74" height="26" viewBox="0 0 74 26" aria-hidden="true"><path d="M0 13 H28 L34 2 L40 24 L45 13 H74" fill="none" stroke="var(--ink)" stroke-width="2.5"/></svg>
  </h2>
  <div class="ddx-cols">
    <ul class="ddx-col">
      <li>Light anesthesia <em>(consider vaporizer or infusion pump empty or malfunctioning)</em></li>
      <li>Hypercarbia</li>
    </ul>
    <ul class="ddx-col">
      <li>Hypoxemia</li>
      <li>Arterial line transducer too low or BP cuff too small</li>
      <li>Withdrawal <em>(EtOH or opioid)</em></li>
    </ul>
    <ul class="ddx-col">
      <li>Thyroid Storm</li>
      <li>Pheochromocytoma</li>
      <li>Drug Error</li>
    </ul>
  </div>
</section>

</body>
</html>
```